Letterhead for small civil engineer company

We need bold and modern design for company letterhead in MS word. It needs to have company logo and company info. Somewhere in the upper right part of document needs to be space for "recever" and the documents starts with, example, "SUBJECT: CIVIL ENGINEER LETTERHEAD".

in the bottom part of document needs to be signature and date.

Company info: Veltrana d.o.o., Lipovac 15, Lipovac (Općina Brdarić), OIB 47396028154, www.veltrana.hr, info@veltrana.hr

Email of document sender needs to be somewhere if document, exapmle xyz@veltrana.hr

Target Market(s)

Civil engineer company and projects

Industry/Entity Type

Civil engineer

Font styles to use
Serif

Colors
F0912C
F2A743
F7CA91
FBE8D2
FDF5EE

Requirements
Must have
• Company logo and company info
Nice to have
• Moder and clean design
Should not have
• Too much details

```html
<!DOCTYPE html>
<html lang="en">
<head>
<meta charset="utf-8">
<title>Veltrana Letterhead</title>
<link href="https://fonts.googleapis.com/css2?family=Open+Sans:wght@400;600&family=Figtree:wght@500;600&display=swap" rel="stylesheet">
<style>
  :root {
    --orange: #f0912c;
    --orange-soft: #fbe8d2;
    --ink: #4a4a4a;
    --ink-dark: #2e2e2e;
    --rule-grey: #6d6d6d;
    --backdrop: #ececee;
    --paper: #ffffff;
  }
  * { margin: 0; padding: 0; box-sizing: border-box; }
  html, body { width: 999px; height: 1200px; overflow: hidden; background: var(--backdrop); }
  body { font-family: "Open Sans", Arial, sans-serif; color: var(--ink); }

  .letterhead {
    position: absolute; left: 70px; top: 0;
    width: 858px; height: 1200px;
    background: var(--paper);
  }

  .brand {
    position: absolute; left: 55px; top: 112px;
    display: flex; align-items: center; gap: 12px;
  }
  .brand-square { width: 22px; height: 22px; background: var(--orange); }
  .brand-name {
    font-family: "Figtree", Arial, sans-serif; font-weight: 600;
    font-size: 30px; letter-spacing: 1px; color: var(--orange);
  }

  .header-rule { position: absolute; left: 55px; top: 190px; }

  .sender { position: absolute; left: 55px; top: 274px; }
  .sender-name { font-size: 23px; font-weight: 600; color: var(--orange); line-height: 28px; }
  .sender-role { font-size: 11px; font-weight: 600; color: var(--ink-dark); margin: 2px 0 8px; }
  .sender-line { font-size: 14.5px; line-height: 24.5px; color: var(--ink-dark); }
  .sender-line b { color: var(--orange); font-weight: 600; display: inline-block; width: 26px; }

  .date { position: absolute; right: 58px; top: 388px; font-size: 14.5px; color: var(--ink-dark); }

  .body-copy { position: absolute; left: 55px; top: 440px; width: 745px; }
  .body-copy p {
    font-size: 14.2px; line-height: 24.5px; text-align: justify;
    margin-bottom: 24.5px; color: var(--ink);
  }

  .signature-area {
    position: absolute; left: 80px; top: 800px; width: 160px; height: 90px;
    background: linear-gradient(135deg, var(--orange-soft), #fdf5ee);
  }
  .signer {
    position: absolute; left: 70px; top: 910px;
    font-family: "Figtree", Arial, sans-serif; font-weight: 500;
    font-size: 22px; color: var(--ink-dark);
  }

  .footer { position: absolute; left: 55px; top: 1084px; font-size: 12.5px; color: var(--ink-dark); font-weight: 600; }
  .footer-row { display: flex; align-items: center; height: 24px; }
  .footer-item { display: flex; align-items: center; gap: 6px; }
  .footer-divider { width: 1px; height: 18px; background: #c9c9c9; margin: 0 12px; }
  .icon { width: 16px; height: 16px; background: var(--orange); border-radius: 3px; display: flex; align-items: center; justify-content: center; }

  .footer-rule { position: absolute; left: 0; top: 1154px; width: 858px; height: 2px; background: var(--orange); }
</style>
</head>
<body>
<main class="letterhead">
  <div class="brand">
    <span class="brand-square"></span>
    <span class="brand-name">VELTRANA</span>
  </div>

  <svg class="header-rule" width="745" height="20" viewBox="0 0 745 20">
    <polygon points="0,0 306,0 313,8 0,8" fill="var(--orange)"/>
    <line x1="313" y1="16" x2="745" y2="16" stroke="var(--rule-grey)" stroke-width="1.5"/>
  </svg>

  <section class="sender">
    <div class="sender-name">Tomas Reed</div>
    <div class="sender-role">Chief Director</div>
    <div class="sender-line"><b>A :</b>1730 Linden Avenue, Fairview, DC 20031</div>
    <div class="sender-line"><b>W :</b>www.veltrana.hr,&nbsp; info@veltrana.hr</div>
    <div class="sender-line"><b>P :</b>OIB 47396028154</div>
  </section>

  <div class="date">12 December, 2024</div>

  <section class="body-copy">
    <p>Lorem ipsum dolor sit amet, consectetuer adipiscing elit, sed diam nonummy nibh euismod tincidunt ut laoreet dolore magna aliquam erat volutpat. Ut wisi enim ad minim veniam, quis nostrud exerci tation ullamcorper suscipit lobortis nisl ut aliquip ex ea commodo consequat. Duis autem vel eum iriure dolor in hendrerit in vulputate velit esse molestie consequat, vel illum dolore eu feugiat nulla facilisis at vero eros et accumsan et iusto odio dignissim qui blandit praesent luptatum zzril delenit augue duis dolore te feugait nulla facilisi.</p>
    <p>Lorem ipsum dolor sit amet, cons ectetuer adipiscing elit, sed diam nonummy nibh euismod tincidunt ut laoreet dolore magna aliquam erat volutpat. Ut wisi enim ad minim veniam, quis nostrud exerci tation ullamcorper suscipit lobortis nisl ut aliquip ex ea commodo consequat.</p>
    <p>Lorem ipsum dolor sit amet, consectetuer adipiscing elit, sed diam nonummy nibh euismod tincidunt ut laoreet dolore magna aliquam erat</p>
  </section>

  <div class="signature-area" role="img" aria-label="Handwritten signature"></div>
  <div class="signer">Mr. Alen Marić</div>

  <footer class="footer">
    <div class="footer-row">
      <span class="footer-item">
        <span class="icon"><svg width="10" height="12" viewBox="0 0 10 12"><path d="M5 0a4 4 0 0 1 4 4c0 3-4 8-4 8S1 7 1 4a4 4 0 0 1 4-4z" fill="#fff"/><circle cx="5" cy="4" r="1.5" fill="var(--orange)"/></svg></span>
        Veltrana d.o.o., Lipovac 15, Lipovac (Općina Brdarić)
      </span>
    </div>
    <div class="footer-row">
      <span class="footer-item">
        <span class="icon"><svg width="10" height="10" viewBox="0 0 10 10"><path d="M2 0l2 2.5-1.2 1.2a6 6 0 0 0 3.5 3.5L7.5 6 10 8l-1.5 2C4 10 0 6 0 1.5z" fill="#fff"/></svg></span>
        OIB 47396028154
      </span>
      <span class="footer-divider"></span>
      <span class="footer-item">
        <span class="icon"><svg width="10" height="8" viewBox="0 0 10 8"><rect x="0.5" y="0.5" width="9" height="7" fill="none" stroke="#fff"/><path d="M0.5 0.5l4.5 4 4.5-4" fill="none" stroke="#fff"/></svg></span>
        info@veltrana.hr
      </span>
      <span class="footer-divider"></span>
      <span class="footer-item">
        <span class="icon"><svg width="10" height="10" viewBox="0 0 10 10"><path d="M1 1l7 3-3 1-1 3z" fill="#fff"/></svg></span>
        www.veltrana.hr
      </span>
    </div>
  </footer>

  <div class="footer-rule"></div>
</main>
</body>
</html>
```